Farhan Dalvesi Business Card

I would like an elegant business card design in both english and arabic.

Ideally a logo design with my name in Arabic (could be a tiger for example)

It should have my Name : Farhan Dalvesi
Title: Advisor / Investor
Tel. UAE +971 558 402 917
UK +44 7812 506 284
Email. farhdalv352@mailvora.com

I am an active angle investor and have many business interests in the TMT space and invest globally, the design needs to be fresh, elegant and striking.

The design should be catching and grab one's attention when they view the card.

Front card should be in English and Reverse in Arabic....

Target Market(s)

Global Investors, CEO's

Industry/Entity Type

Business

Contact Information for Business Card

Title: Advisor / Investor
Tel. UAE +971 558 402 917
UK +44 7812 506 284

Font styles to use
Serif
Other font styles liked:
• Palantino

Requirements
Must have
• A striking design with a play of my name in Arabic, could be my name that is designed as a tiger for example

```html
<!DOCTYPE html>
<html lang="en">
<head>
<meta charset="utf-8">
<title>Farhan Dalvesi Business Card</title>
<link rel="stylesheet" href="https://fonts.googleapis.com/css2?family=Amiri:wght@400;700&family=Tinos:wght@400;700&display=swap">
<style>
  :root {
    --backdrop: #6e7f86;
    --card: #ffffff;
    --ink: #111416;
    --slate: #6b7880;
    --title-grey: #7a8a90;
    --mist: #d7dcdd;
    --side-grey: #a7b2b6;
    --peach: #f3d3b6;
    --sky: #8fcdf0;
    --sky-deep: #6aaedb;
    --lime: #cfe9a8;
    --lime-deep: #b9de86;
    --art: #9aa3a6;
  }
  html, body {
    margin: 0;
    width: 1200px;
    height: 1000px;
    overflow: hidden;
    background: var(--backdrop);
  }
  .card {
    position: absolute;
    left: 358px;
    width: 510px;
    height: 299px;
    background: var(--card);
  }
  .card--front { top: 137px; }
  .card--back { top: 499px; }
  .card svg { display: block; width: 510px; height: 299px; }
  .serif { font-family: 'Tinos', 'Palatino Linotype', Palatino, serif; }
  .script { font-family: 'Amiri', 'Palatino Linotype', serif; }
  .name { font-size: 20px; font-weight: 700; fill: var(--ink); letter-spacing: 0.5px; }
  .title { font-size: 15px; font-weight: 700; fill: var(--title-grey); letter-spacing: 0.5px; }
  .contact { font-size: 16px; font-weight: 700; fill: var(--ink); }
  .mark-name { font-size: 17px; font-weight: 400; fill: var(--ink); letter-spacing: 1px; }
</style>
</head>
<body>

<div class="card card--front">
  <svg viewBox="0 0 510 299" xmlns="http://www.w3.org/2000/svg">
    <circle cx="392" cy="38" r="140" fill="var(--mist)"/>
    <circle cx="392" cy="38" r="128" fill="none" stroke="#fff" stroke-width="2" opacity="0.7"/>
    <circle cx="-28" cy="205" r="116" fill="none" stroke="var(--peach)" stroke-width="2"/>
    <circle cx="-28" cy="205" r="108" fill="var(--side-grey)"/>
    <rect class="tiger-watermark" x="352" y="125" width="135" height="172" rx="60" fill="var(--art)" opacity="0.12" role="img" aria-label="Faint tiger head line illustration"/>
    <path d="M0 272 C140 262 300 250 510 190 L510 299 L0 299 Z" fill="var(--sky)" opacity="0.75"/>
    <path d="M0 284 C160 278 330 268 510 226 L510 299 L0 299 Z" fill="var(--sky-deep)" opacity="0.7"/>
    <rect x="198" y="76" width="312" height="4" fill="var(--slate)"/>
    <text class="serif name" x="270" y="70">Farhan Dalvesi</text>
    <text class="serif title" x="265" y="94">Advisor / Investor</text>
    <rect class="tiger-illustration" x="94" y="28" width="94" height="82" rx="30" fill="var(--art)" opacity="0.55" role="img" aria-label="Tiger head line illustration"/>
    <text class="serif mark-name" x="55" y="130">Farhan</text>
    <text class="serif mark-name" x="108" y="152">Dalvesi</text>
    <g fill="#fff" stroke="#fff">
      <path d="M61 209 q-3 6 2 12 l3 -2 q-3 -4 -1 -8 z" stroke-width="1"/>
      <rect x="58" y="246" width="15" height="10" fill="none" stroke-width="1.5"/>
      <path d="M58 246 l7.5 6 l7.5 -6" fill="none" stroke-width="1.5"/>
    </g>
    <text class="serif contact" x="92" y="222">UAE</text>
    <text class="serif contact" x="146" y="222">+971 558 402 917</text>
    <text class="serif contact" x="95" y="238">UK</text>
    <text class="serif contact" x="146" y="238">+44 7812 506 284</text>
    <text class="serif contact" x="90" y="255">farhdalv352@mailvora.com</text>
  </svg>
</div>

<div class="card card--back">
  <svg viewBox="0 0 510 299" xmlns="http://www.w3.org/2000/svg">
    <circle cx="392" cy="38" r="140" fill="var(--mist)"/>
    <circle cx="392" cy="38" r="128" fill="none" stroke="#fff" stroke-width="2" opacity="0.7"/>
    <circle cx="-28" cy="205" r="116" fill="none" stroke="var(--peach)" stroke-width="2"/>
    <circle cx="-28" cy="205" r="108" fill="var(--side-grey)"/>
    <rect class="tiger-watermark" x="362" y="125" width="135" height="172" rx="60" fill="var(--art)" opacity="0.12" role="img" aria-label="Faint tiger head line illustration"/>
    <path d="M0 272 C140 262 300 250 510 190 L510 299 L0 299 Z" fill="var(--lime)" opacity="0.8"/>
    <path d="M0 284 C160 278 330 268 510 226 L510 299 L0 299 Z" fill="var(--lime-deep)" opacity="0.5"/>
    <rect x="198" y="76" width="312" height="4" fill="var(--slate)"/>
    <text class="script name" x="266" y="70">Farhan Dalvesi</text>
    <text class="script title" x="262" y="94">Advisor / Investor</text>
    <rect class="tiger-illustration" x="94" y="28" width="94" height="82" rx="30" fill="var(--art)" opacity="0.55" role="img" aria-label="Tiger head line illustration"/>
    <text class="serif mark-name" x="55" y="130">Farhan</text>
    <text class="serif mark-name" x="108" y="152">Dalvesi</text>
    <g fill="#fff" stroke="#fff">
      <path d="M61 209 q-3 6 2 12 l3 -2 q-3 -4 -1 -8 z" stroke-width="1"/>
      <rect x="58" y="246" width="15" height="10" fill="none" stroke-width="1.5"/>
      <path d="M58 246 l7.5 6 l7.5 -6" fill="none" stroke-width="1.5"/>
    </g>
    <text class="script contact" x="92" y="220">UAE</text>
    <text class="script contact" x="140" y="220">+971 558 402 917</text>
    <text class="script contact" x="94" y="237">UK</text>
    <text class="script contact" x="140" y="237">+44 7812 506 284</text>
    <text class="script contact" x="90" y="254">farhdalv352@mailvora.com</text>
  </svg>
</div>

</body>
</html>
```